KELBROOK PAINTING

We are a painting company. We paint residential, commercial and strata jobs. I need the website to be very sharp, neat and elegant. I've attached our logo. the Logo needs to be embossed as a gold color and the background like a Matt black. I need these tabs:

• HOME • ABOUT US • SERVICES • TESTIMONIALS • SHOWCASE • CONTACT US

Be creative and innovative in your style.
take this as an example to just get the gist of what I'm expecting. If you can better it then the job is yours!

http://gilmarchcoatings.com.au/contact.html

I look forward to seeing your artwork :)

#These are the links to my logo in PSD format.

https://www.filevaultzy.com/s/qrtxwpl3k8hvb2z/Kelbrook%20Painting%20Luxury%20Gold.rar

https://www.filevaultzy.com/sh/hvbdkwpa2m7ycq5/XuoP7-bqLk

Painting

• Making the Logo embossed like the artworks i have attached is definitely a necessity.

Can you let me know if this is possible to apply to the website.

thank you

```html
<!DOCTYPE html>
<html lang="en">
<head>
<meta charset="utf-8">
<title>Kelbrook Painting</title>
<link href="https://fonts.googleapis.com/css2?family=PT+Sans+Narrow:wght@400;700&family=Source+Sans+3:wght@300;400;600;700&display=swap" rel="stylesheet">
<style>
:root{
  --gold:#c9a445;
  --gold-light:#dcbf6e;
  --gold-dark:#a8832a;
  --gold-text:#d9a21f;
  --ink:#2f2f2f;
  --body:#5b5b5b;
  --panel:#ffffff;
  --footer-top:#3a3a3a;
  --footer-bottom:#1b1b1b;
}
*{margin:0;padding:0;box-sizing:border-box}
html,body{width:1200px;height:1086px;overflow:hidden}
body{position:relative;background:var(--panel);font-family:"Source Sans 3",sans-serif;color:var(--body)}
.top-stripe{position:absolute;left:0;top:0;width:1200px;height:7px;
  background:repeating-linear-gradient(90deg,var(--gold-dark) 0 150px,var(--gold-light) 150px 300px)}
.brand{position:absolute;left:113px;top:27px;display:flex;align-items:center}
.brand-mark{width:90px;height:90px;border:3px solid var(--gold);border-radius:50%}
.brand-name{position:absolute;left:101px;top:29px;font-weight:700;font-size:27px;color:var(--ink);white-space:nowrap;letter-spacing:-0.3px}
.brand-tagline{position:absolute;left:143px;top:57px;font-size:12.5px;color:var(--ink);white-space:nowrap}
.call{position:absolute;right:124px;top:62px;text-align:right;color:var(--ink)}
.call-label{font-size:20px;font-weight:400;line-height:1}
.call-number{font-size:30px;font-weight:400;line-height:1.15}
.main-nav{position:absolute;left:106px;top:135px;width:986px;height:49px;display:flex;
  background:linear-gradient(180deg,var(--gold-light),var(--gold) 45%,var(--gold-dark));border-radius:3px 3px 0 0}
.main-nav a{display:flex;align-items:center;justify-content:center;color:#fff;text-decoration:none;
  font-family:"PT Sans Narrow",sans-serif;font-size:20px;border-right:1px solid rgba(255,255,255,.35)}
.main-nav a:last-child{border-right:none}
.hero{position:absolute;left:106px;top:184px;width:986px;height:372px;
  background:linear-gradient(90deg,#cdb98a 0%,#7ccf1c 30%,#e9e7e2 42%,#7fcb10 65%,#d8d320 85%,#6ab50e 100%)}
.hero-caption{position:absolute;left:642px;top:203px;width:320px;height:108px;background:rgba(255,255,255,.86);padding:16px 0 0 30px;
  font-family:"PT Sans Narrow",sans-serif;line-height:1;white-space:nowrap;overflow:hidden}
.hero-caption .kicker{font-size:30px;font-weight:700;color:var(--gold-text)}
.hero-caption .title{font-size:34px;font-weight:700;color:var(--ink);margin-top:6px}
.hero-dots{position:absolute;left:442px;top:348px;display:flex;gap:4px}
.hero-dots span{width:13px;height:13px;border-radius:50%;background:#fff}
.content{position:absolute;left:0;top:556px;width:1200px}
.welcome-title{position:absolute;left:139px;top:32px;font-family:"PT Sans Narrow",sans-serif;font-size:31px;font-weight:400;color:var(--ink);white-space:nowrap;line-height:1.2}
.welcome-photo{position:absolute;left:141px;top:74px;width:159px;height:159px;background:linear-gradient(160deg,#e25b4c,#f2d3c9 55%,#8aa1b8)}
.copy{font-size:12.6px;line-height:22.3px;font-weight:300;color:var(--body)}
.copy p{margin-bottom:8px}
.copy-side{position:absolute;left:313px;top:74px;width:470px}
.copy-full{position:absolute;left:140px;top:254px;width:640px}
.services{position:absolute;left:808px;top:32px;width:267px;height:312px;background:var(--gold);border-radius:3px}
.services h2{height:46px;background:linear-gradient(180deg,var(--gold-light),var(--gold-dark));
  font-family:"PT Sans Narrow",sans-serif;font-weight:400;font-size:22px;color:#fff;padding:10px 0 0 30px;border-radius:3px 3px 0 0}
.services ul{list-style:none;margin:10px 26px 0 21px}
.services li{height:33.5px;border-bottom:1px solid rgba(255,255,255,.25);color:#fff;font-size:13.5px;display:flex;align-items:center;padding-left:16px;position:relative}
.services li:last-child{border-bottom:none}
.services li::before{content:"";position:absolute;left:2px;top:12px;border-left:5px solid #fff;border-top:5px solid transparent;border-bottom:5px solid transparent}
.site-footer{position:absolute;left:0;top:955px;width:1200px;height:131px;background:linear-gradient(180deg,var(--footer-top),var(--footer-bottom))}
.footer-nav{position:absolute;left:132px;top:26px;font-family:"Source Sans 3",sans-serif;font-size:13.5px;color:#fff;white-space:nowrap}
.footer-nav span{margin:0 4px}
.copyright{position:absolute;left:132px;top:58px;font-size:10.5px;color:#ddd}
.social{position:absolute;left:959px;top:30px;display:flex;gap:4px}
.social span{width:27px;height:27px;border-radius:50%;background:#fff}
</style>
</head>
<body>
<div class="top-stripe"></div>

<header>
  <div class="brand">
    <div class="brand-mark"></div>
    <div class="brand-name">KELBROOK PAINTING</div>
    <div class="brand-tagline">Painting Australia Everyday!</div>
  </div>
  <div class="call">
    <div class="call-label">Call Us Now</div>
    <div class="call-number">0400 555 017</div>
  </div>
  <nav class="main-nav">
    <a style="width:139px">HOME</a>
    <a style="width:156px">ABOUT US</a>
    <a style="width:149px">SERVICES</a>
    <a style="width:186px">TESTIMONIALS</a>
    <a style="width:162px">SHOWCASE</a>
    <a style="width:194px">CONTACT US</a>
  </nav>
</header>

<section class="hero" role="img" aria-label="Photo of a bright green and yellow painted children's bedroom with bunk bed and shelving">
  <div class="hero-caption">
    <div class="kicker">QUALITY &amp; SERVICES</div>
    <div class="title">KELBROOK PAINTING</div>
  </div>
  <div class="hero-dots"><span></span><span></span><span></span><span></span></div>
</section>

<main class="content">
  <h1 class="welcome-title">WELCOME TO OUR WEBSITE MAINPAGE..</h1>
  <div class="welcome-photo" role="img" aria-label="Photo of a couple painting a wall red with paint tins"></div>
  <div class="copy copy-side">
    <p>Nulla elementum dui ut augue. Aliquam vehicula mi at mauris. Maecenas placerat, nisl at consequat rhoncus, sem nunc gravida justo, quis eleifend arcu velit quis lacus. Morbi magna magna, tincidunt a, mattis non, imperdiet vitae, tellus. Sed odio est, auctor ac, sollicitudin in, consequat vitae, orci. Fusce id felis. Vivamus sollicitudin metus eget eros.</p>
    <p>Mauris vel lacus vitae felis vestibulum volutpat. Etiam est nunc, venenatis in, tristique eu, imperdiet ac, nisl. Cum sociis natoque penatibus et magnis dis parturient montes, nascetur ridiculus mus.</p>
  </div>
  <div class="copy copy-full">
    <p>Nulla elementum dui ut augue. Aliquam vehicula mi at mauris. Maecenas placerat, nisl at consequat rhoncus, sem nunc gravida justo, quis eleifend arcu velit quis lacus. Morbi magna magna, tincidunt a, mattis non, imperdiet vitae, tellus. Sed odio est, auctor ac, sollicitudin in, consequat vitae, orci. Fusce id felis. Vivamus sollicitudin metus eget eros.</p>
    <p>Mauris vel lacus vitae felis vestibulum volutpat. Etiam est nunc, venenatis in, tristique eu, imperdiet ac, nisl.</p>
  </div>
  <aside class="services">
    <h2>SERVICES PROVIDE</h2>
    <ul>
      <li>Phasellus felis dolor</li>
      <li>Scelerisque tempus eget</li>
      <li>Lobortis id libero</li>
      <li>Donec scelerisque leo</li>
      <li>Praesent sit amet est.</li>
      <li>Dictum dolor dictum</li>
      <li>Porttitor enim felis viverra</li>
    </ul>
  </aside>
</main>

<footer class="site-footer">
  <div class="footer-nav">HOME<span>|</span>ABOUT US<span>|</span>SERVICES<span>|</span>TESTIMONIALS<span>|</span>SHOWCASE<span>|</span>CONTACT US</div>
  <div class="copyright">© 2012 Company Name.&nbsp; All right reserved.&nbsp; Term of Use</div>
  <div class="social"><span></span><span></span><span></span><span></span></div>
</footer>
</body>
</html>
```